Criação de Logo e Papelaria (6 itens) para Reabilitaçao Oral/Periodontia/Implantodontia com credenciamento em cirurgia guiada por computador.
" Profissional liberal: cirurgiao- dentista especialista em periodontia e implantodontia. "

```html
<!DOCTYPE html>
<html lang="pt-BR">
<head>
<meta charset="utf-8">
<title>Papel Timbrado — Dr. Rafael Montenegro</title>
<link href="https://fonts.googleapis.com/css2?family=Lato:wght@400;700&display=swap" rel="stylesheet">
<style>
  :root {
    --backdrop: #e6e6e4;
    --paper: #ffffff;
    --teal: #4fd0cb;
    --teal-deep: #2aa9a6;
    --teal-faint: #e4f4f3;
    --ink-teal: #1c8a89;
    --white: #ffffff;
  }
  html, body {
    margin: 0;
    width: 1200px;
    height: 1200px;
    overflow: hidden;
    background: var(--backdrop);
    font-family: "Lato", Arial, sans-serif;
  }
  .letterhead {
    position: absolute;
    left: 248px;
    top: 100px;
    width: 704px;
    height: 1000px;
    background: var(--paper);
    box-shadow: 0 2px 10px rgba(0,0,0,0.15);
    overflow: hidden;
  }
  .brand {
    position: absolute;
    left: 24px;
    top: 42px;
    width: 150px;
    display: flex;
    flex-direction: column;
    align-items: center;
  }
  .brand-mark {
    width: 30px;
    height: 30px;
    border-radius: 50%;
    background: var(--teal);
    margin-bottom: 10px;
  }
  .brand-name {
    font-size: 14px;
    font-weight: 700;
    color: var(--ink-teal);
    white-space: nowrap;
  }
  .brand-tagline {
    margin-top: 2px;
    font-size: 6px;
    letter-spacing: 1.6px;
    text-transform: uppercase;
    color: var(--ink-teal);
    white-space: nowrap;
  }
  .corner-accent {
    position: absolute;
    left: 480px;
    top: 740px;
    width: 240px;
    height: 240px;
  }
  .footer-band {
    position: absolute;
    left: 0;
    top: 916px;
    width: 100%;
    height: 50px;
    background: var(--teal);
  }
  .footer-contact {
    position: absolute;
    left: 14px;
    top: 5px;
    margin: 0;
    font-size: 10px;
    line-height: 13px;
    color: var(--white);
    font-style: normal;
  }
</style>
</head>
<body>
  <main class="letterhead">
    <header class="brand">
      <span class="brand-mark" aria-hidden="true"></span>
      <span class="brand-name">Dr. Rafael Montenegro</span>
      <span class="brand-tagline">Reabilitação Oral</span>
    </header>

    <svg class="corner-accent" viewBox="0 0 240 240" aria-hidden="true">
      <circle cx="115" cy="110" r="105" fill="var(--teal-faint)"/>
    </svg>

    <footer class="footer-band">
      <address class="footer-contact">
        Rua das Acácias nº 215 São Paulo SP<br>
        11 4020 1357 / 11 4020 2468<br>
        rafael.odonto@mail.com
      </address>
    </footer>
  </main>
</body>
</html>
```